Industrial Project Sign

We need an eye catching (but professional) industrial project sign that will be very large (roughly 12' high x 18' wide). This sign will be highly visible from the adjacent high speed highway.

* The following needs to be at the bottom of the signage: Logo (uploaded), Name (Pillar Ventures Group, Inc.) (uploaded) and phone number (555)613-8874

*Name of Project - "Brambleford Industrial Center"

* Text items
Land for Sale
Build to Suit
Zoning: Industrial (G I & L I)

* Interesting background that is eye catching
Updates

Good morning all,

We are considering all designers options as we go and are waiting for the final designs to come in by the 4th so that we can give each one a good look.   If you have any new designs, questions, further design options or any tweeks you want to do to current designs, please do so at this time.

Thanks to all of you for your submissions.

Industry/Entity Type

Industrial

```html
<!DOCTYPE html>
<html lang="en">
<head>
<meta charset="utf-8">
<title>Brambleford Industrial Center – Project Sign</title>
<link rel="stylesheet" href="https://fonts.googleapis.com/css2?family=Open+Sans:wght@400;600;700;800&display=swap">
<style>
  :root {
    --sign-bg: #e6e7e8;
    --ink: #111111;
    --maroon: #6d1517;
    --grey-band: #6a6a6a;
    --grey-text: #5e5e5e;
    --dot-grey: #8a8a8a;
    --white: #ffffff;
  }
  * { margin: 0; padding: 0; box-sizing: border-box; }
  html, body { width: 1200px; height: 800px; overflow: hidden; background: var(--sign-bg); }
  .sign {
    position: relative;
    width: 1200px; height: 800px;
    background: var(--sign-bg);
    font-family: "Open Sans", Arial, sans-serif;
  }
  .project-name {
    position: absolute; top: 18px; left: 0; width: 100%;
    text-align: center;
    font-size: 55px; font-weight: 700; letter-spacing: 1px;
    color: var(--ink); line-height: 76px;
  }
  .dot-rule {
    position: absolute; left: 82px; width: 1050px; height: 10px;
    background-image:
      radial-gradient(circle at 5px 5px, var(--dot-grey) 4px, transparent 4.5px),
      radial-gradient(circle at 5px 5px, var(--maroon) 3px, transparent 3.5px);
    background-size: 44px 10px, 44px 10px;
    background-position: 0 0, 22px 0;
    background-repeat: repeat-x;
  }
  .dot-rule--top { top: 91px; }
  .dot-rule--bottom { top: 706px; }

  .offer-banner {
    position: absolute; top: 131px; left: 0; width: 1200px; height: 85px;
  }
  .offer-banner svg { position: absolute; inset: 0; }
  .offer {
    position: absolute; top: 0; height: 85px; line-height: 85px;
    color: var(--white); font-weight: 700; font-size: 62px; letter-spacing: 0.5px;
  }
  .offer--sale { left: 30px; }
  .offer--build { left: 660px; }

  .site-photo {
    position: absolute; top: 216px; left: 0; width: 1200px; height: 217px;
    background: linear-gradient(90deg, #b89a6c 0%, #a77d58 35%, #b07a5a 55%, #9aa0a6 78%, #b9bcc2 100%);
  }

  .zoning-band {
    position: absolute; top: 433px; left: 0; width: 1200px; height: 83px;
    background: var(--grey-band);
    color: var(--white); text-align: center;
    font-size: 58px; font-weight: 700; line-height: 83px; letter-spacing: 0.5px;
  }

  .brand-mark {
    position: absolute; top: 548px; left: 330px; width: 100px; height: 100px;
    background: var(--maroon);
  }
  .company-name {
    position: absolute; top: 578px; left: 474px;
    font-size: 27px; font-weight: 600; color: var(--grey-text); line-height: 36px;
  }
  .company-rule {
    position: absolute; top: 619px; left: 470px; width: 452px; height: 4px;
    background: var(--maroon);
  }
  .company-phone {
    position: absolute; top: 617px; left: 468px;
    font-size: 60px; font-weight: 700; color: var(--ink); line-height: 80px;
  }

  .website {
    position: absolute; top: 724px; left: 0; width: 100%;
    text-align: center; font-size: 47px; font-weight: 700; line-height: 66px;
    color: var(--grey-text); letter-spacing: 0.5px;
  }
  .website__domain { color: var(--maroon); }
</style>
</head>
<body>
<main class="sign">
  <h1 class="project-name">BRAMBLEFORD INDUSTRIAL CENTER</h1>
  <div class="dot-rule dot-rule--top"></div>

  <section class="offer-banner">
    <svg width="1200" height="85" viewBox="0 0 1200 85" aria-hidden="true">
      <polygon points="0,0 640,0 610,85 0,85" fill="#6d1517"/>
      <polygon points="640,0 1200,0 1200,85 610,85" fill="#000000"/>
    </svg>
    <span class="offer offer--sale">LAND FOR SALE</span>
    <span class="offer offer--build">BUILD TO SUIT</span>
  </section>

  <div class="site-photo" role="img" aria-label="Photo of a row of stucco buildings with terracotta roofs under a grey sky"></div>

  <div class="zoning-band">ZONING: INDUSTRIAL (G I &amp; L I)</div>

  <div class="brand-mark"></div>
  <p class="company-name">Pillar Ventures Group, Inc.</p>
  <div class="company-rule"></div>
  <p class="company-phone">(555)613-8874</p>

  <div class="dot-rule dot-rule--bottom"></div>
  <p class="website">WWW.<span class="website__domain">PILLARVENTURESGROUP</span>.COM</p>
</main>
</body>
</html>
```